Real Estate Listing Signs for standard Yard arms

I need real estate listing signs done, for the standard sized sign to be hung beneath a white yard arm. To match existing logo. Information to be included:
-Logo
-Business name
-Phone number
-Marden Fosk Tundra Circle & Marden Fosk realty logos (smaller print)

Colors to be Red and anywhere in the gray scale between black and white, or a combination of those.

Target Market(s)

Drive by visuals

Industry/Entity Type

Real Estate Agent

Colors

Designer to choose only greyscale colors for use in the design.

Requirements
Must have
• My Logo and business name in same/similar font to whats provided, the MF tundra circle logo (small on bottom or corner somewhere), My phone number, and a decent amount of red coloration on the sign.

```html
<!DOCTYPE html>
<html lang="en">
<head>
<meta charset="utf-8">
<title>Brandvik Realty – Yard Sign</title>
<link rel="stylesheet" href="https://fonts.googleapis.com/css2?family=Open+Sans:wght@400;700;800&family=Oswald:wght@700&family=Roboto+Condensed:wght@400&display=swap">
<style>
  :root {
    --stage: #d9d9d9;
    --panel-top: #ffffff;
    --panel-bottom: #e4e4e4;
    --ink: #111111;
    --red: #d4101c;
    --gray: #6a6a6a;
  }
  * { margin: 0; padding: 0; box-sizing: border-box; }
  html, body {
    width: 1200px;
    height: 905px;
    overflow: hidden;
    background: var(--stage);
  }
  .canvas {
    position: relative;
    width: 1200px;
    height: 905px;
  }
  .sign {
    position: absolute;
    left: 310px;
    top: 14px;
    width: 580px;
    height: 876px;
    background: linear-gradient(180deg, var(--panel-top) 0%, var(--panel-top) 35%, var(--panel-bottom) 100%);
    box-shadow: 0 4px 18px rgba(0,0,0,0.18);
  }
  .band {
    position: absolute;
    top: 152px;
    height: 160px;
  }
  .band--black { left: 0; width: 173px; background: var(--ink); }
  .band--red { right: 0; width: 182px; background: var(--red); }
  .brand-mark {
    position: absolute;
    left: 173px;
    width: 225px;
    top: 152px;
    height: 160px;
    display: flex;
    align-items: center;
    justify-content: center;
    font-family: "Open Sans", sans-serif;
    font-weight: 800;
    font-size: 38px;
    letter-spacing: 1px;
    color: var(--red);
  }
  .business-name {
    position: absolute;
    left: 0;
    width: 100%;
    text-align: center;
    font-family: "Open Sans", sans-serif;
    font-weight: 800;
    font-size: 80px;
    line-height: 1;
    color: var(--ink);
    letter-spacing: 1px;
  }
  .business-name--first { top: 340px; }
  .business-name--second { top: 444px; }
  .divider {
    position: absolute;
    left: 232px;
    width: 116px;
    height: 2px;
    background: var(--ink);
  }
  .divider--upper { top: 551px; }
  .divider--lower { top: 736px; }
  .phone {
    position: absolute;
    top: 578px;
    left: 0;
    width: 100%;
    text-align: center;
    font-family: "Oswald", sans-serif;
    font-weight: 700;
    font-size: 72px;
    line-height: 1;
    color: var(--red);
  }
  .website {
    position: absolute;
    top: 661px;
    left: 0;
    width: 100%;
    text-align: center;
    font-family: "Open Sans", sans-serif;
    font-weight: 400;
    font-size: 37px;
    line-height: 1;
    color: var(--ink);
    letter-spacing: 1px;
  }
  .brokerage {
    position: absolute;
    top: 764px;
    left: 0;
    width: 100%;
    text-align: center;
    font-family: "Roboto Condensed", sans-serif;
    font-weight: 400;
    color: var(--gray);
  }
  .brokerage__name {
    display: block;
    font-size: 34px;
    line-height: 1;
  }
  .brokerage__sub {
    display: block;
    margin-top: 6px;
    font-size: 15px;
    letter-spacing: 1px;
    line-height: 1;
  }
</style>
</head>
<body>
  <main class="canvas">
    <section class="sign" aria-label="Brandvik Realty listing sign">
      <div class="band band--black"></div>
      <div class="brand-mark">BRANDVIK</div>
      <div class="band band--red"></div>

      <h1 class="business-name business-name--first">BRANDVIK</h1>
      <h1 class="business-name business-name--second">REALTY</h1>

      <div class="divider divider--upper"></div>
      <p class="phone">(907)-555-0148</p>
      <p class="website">BRANDVIKREALTY.COM</p>
      <div class="divider divider--lower"></div>

      <p class="brokerage">
        <span class="brokerage__name">MF TUNDRA CIRCLE</span>
        <span class="brokerage__sub">MARDEN FOSK REALTY</span>
      </p>
    </section>
  </main>
</body>
</html>
```